The Pixel Tavern Business card.

A Simple card with our Logo and contact information. To give to investors and other professionals.

We are a nerd themed bar.
our target market is young professionals age 21+ but the real purpose of this business card is to present to potential investors and other professionals with our contact information. as we are still looking for funding before we start up.

I am partial to green and my partner likes red we are open to iteration.

Target Market(s)

Investors

Industry/Entity Type

Business

Contact Information for Business Card

Marcus Henley (555) 730-6621 kent.w4100@mailbox-demo.net Brian Tolle (555) 918-2047 briant731@mailbox-demo.net

Font styles to use
Serif

Requirements
Nice to have
• Keep it simple but not boring.
• Use the Logos but feel free to edit them to match theme/colors.
• Keep the back clean and use one of the Logos.

```html
<!DOCTYPE html>
<html lang="en">
<head>
<meta charset="utf-8">
<title>The Pixel Tavern — Business Card</title>
<link rel="stylesheet" href="https://fonts.googleapis.com/css2?family=Montserrat:wght@400;600;800&display=swap">
<style>
  :root {
    --backdrop: #e9e6e1;
    --card: #ffffff;
    --ink: #111111;
    --muted: #7a7a7a;
    --accent: #e8434f;
    --band: #1a1a1a;
    --rule: #e3e3e3;
  }
  * { box-sizing: border-box; margin: 0; padding: 0; }
  html, body {
    width: 1200px; height: 950px; overflow: hidden;
    background: var(--backdrop);
    font-family: "Montserrat", sans-serif;
  }
  .stage { position: relative; width: 1200px; height: 950px; }

  .card {
    position: absolute;
    width: 560px; height: 320px;
    background: var(--card);
    box-shadow: 0 10px 30px rgba(0,0,0,.18);
    overflow: hidden;
  }
  .card--front { left: 120px; top: 70px; }
  .card--back  { left: 520px; top: 520px; }

  /* Front */
  .front-mark {
    position: absolute; inset: 0;
    display: flex; align-items: center; justify-content: center; gap: 24px;
  }
  .mark-dot {
    width: 54px; height: 54px; border-radius: 50%;
    background: var(--accent); flex: none;
  }
  .mark-name {
    font-weight: 800; color: var(--ink);
    font-size: 58px; line-height: .95; letter-spacing: 1px;
    text-transform: uppercase;
  }

  /* Back */
  .back-mark {
    position: absolute; left: 40px; top: 108px;
    display: flex; align-items: center; gap: 12px;
  }
  .back-mark .mark-dot { width: 24px; height: 24px; }
  .back-mark .mark-name { font-size: 26px; }

  .divider {
    position: absolute; left: 262px; top: 40px;
    width: 1px; height: 140px; background: var(--rule);
  }
  .contact {
    position: absolute; left: 286px; top: 54px;
    color: var(--muted); font-size: 13px;
  }
  .contact-name {
    font-weight: 600; color: #333; font-size: 18px;
    letter-spacing: .5px; text-transform: uppercase; margin-bottom: 14px;
  }
  .contact-line { display: flex; align-items: center; gap: 10px; margin-bottom: 8px; white-space: nowrap; }
  .contact-line svg { width: 13px; height: 13px; flex: none; }

  .bands { position: absolute; left: 0; bottom: 0; width: 560px; height: 120px; }
</style>
</head>
<body>
<main class="stage">

  <section class="card card--front" aria-label="Card front">
    <div class="front-mark">
      <span class="mark-dot"></span>
      <span class="mark-name">The Pixel<br>Tavern</span>
    </div>
  </section>

  <section class="card card--back" aria-label="Card back">
    <div class="back-mark">
      <span class="mark-dot"></span>
      <span class="mark-name">The Pixel<br>Tavern</span>
    </div>

    <div class="divider"></div>

    <div class="contact">
      <p class="contact-name">Marcus Henley</p>
      <p class="contact-line">
        <svg viewBox="0 0 14 14" aria-hidden="true"><rect x="3.5" y="1" width="7" height="12" rx="1.2" fill="none" stroke="#555" stroke-width="1.3"/><rect x="6" y="10.6" width="2" height="1" fill="#555"/></svg>
        (555) 730-6621
      </p>
      <p class="contact-line">
        <svg viewBox="0 0 14 14" aria-hidden="true"><rect x="1" y="3" width="12" height="8.5" fill="#555"/><path d="M1 3.5 L7 8 L13 3.5" fill="none" stroke="#fff" stroke-width="1.1"/></svg>
        kent.w4100@mailbox-demo.net
      </p>
    </div>

    <svg class="bands" viewBox="0 0 560 120" preserveAspectRatio="none" aria-hidden="true">
      <polygon points="0,72 560,40 560,120 0,120" fill="var(--band)"/>
      <polygon points="400,49 560,40 560,22 400,31" fill="var(--accent)"/>
      <polygon points="400,49 560,40 560,48 400,57" fill="#b8323c"/>
    </svg>
  </section>

</main>
</body>
</html>
```